Redesign Employer Form

We need to consolidate the form located at: BrambleQuarry.com to be one form instead of the multiple screens that currently exist. The new form must be user friendly with a layout that supports the collection of the various pieces of information currently displayed on the site.

```html
<!DOCTYPE html>
<html lang="en">
<head>
<meta charset="utf-8">
<title>BrambleQuarry – Salaried Employee Form</title>
<link rel="stylesheet" href="https://fonts.googleapis.com/css2?family=Roboto:wght@300;400;500;700&display=swap">
<style>
:root{
  --bg-stage:#3c4d57;
  --header-blue:#1f4fa8;
  --header-deep:#123a88;
  --page:#eef3f6;
  --field:#ffffff;
  --field-border:#dde3e8;
  --label:#8a949c;
  --text:#333a40;
  --heading:#2d3438;
  --error:#e8333a;
  --ok:#4cb848;
  --link:#2a86d6;
  --accent:#ee5228;
  --footer:#e2e8ec;
  --footer-text:#8d969d;
  --badge-green:#5cb82c;
  --badge-ink:#10222b;
  --envelope:#f4c51a;
}
*{box-sizing:border-box;margin:0;padding:0}
html,body{width:1200px;height:1200px;overflow:hidden}
body{background:var(--page);font-family:'Roboto',sans-serif;color:var(--text)}
.screen{position:absolute;left:0;top:0;width:956px;height:956px;transform:scale(1.2552);transform-origin:0 0;background:var(--page);overflow:hidden}
.abs{position:absolute}
/* header */
.site-header{left:0;top:0;width:956px;height:72px;background:linear-gradient(90deg,var(--header-deep),var(--header-blue) 50%,var(--header-deep))}
.brand-dot{left:111px;top:8px;width:55px;height:55px;border-radius:50%;background:#f1ece4;border:3px solid #fff}
.brand-name{left:180px;top:18px;color:#fff;font-weight:700;font-size:28px;letter-spacing:-.3px}
.brand-tld{left:332px;top:50px;color:#fff;font-weight:700;font-size:9px}
.promo{left:556px;top:0;width:72px;height:72px;border-radius:50%;background:var(--badge-green);border:2px solid #fff;display:flex;flex-direction:column;align-items:center;justify-content:center;font-weight:700;line-height:1.05}
.promo .promo-line{font-size:11px;color:var(--badge-ink)}
.promo .promo-price{font-size:15px;color:#fff;margin-top:3px}
.region-map{left:700px;top:0;width:170px;height:72px;background:radial-gradient(ellipse at 55% 60%,rgba(70,130,90,.75),rgba(40,90,110,.35) 55%,transparent 72%)}
/* title */
.page-title{left:0;width:956px;top:112px;text-align:center;font-weight:300;font-size:29px;color:var(--heading)}
.page-sub{left:0;width:956px;top:150px;text-align:center;font-size:8.5px;color:var(--heading)}
.section-title{font-size:11.5px;font-weight:500;color:var(--heading)}
.error-line{left:113px;top:235px;font-size:7px;color:var(--error);display:flex;align-items:center;gap:9px;font-weight:500}
.err-icon{width:10px;height:10px;border-radius:50%;background:var(--error);color:#fff;font-size:7px;line-height:10px;text-align:center}
.field{position:absolute;height:35px;background:var(--field);border:1px solid var(--field-border);box-shadow:0 1px 2px rgba(0,0,0,.06);padding:0 12px;display:flex;flex-direction:column;justify-content:center;font-size:8px;color:var(--label)}
.field .label{font-size:6.5px}
.field .value{font-size:8px;color:var(--text);margin-top:3px}
.field.invalid{border-color:var(--error)}
.field.invalid .value{color:var(--error)}
.field.valid{border-color:var(--ok)}
.req{position:absolute;right:9px;top:6px;color:var(--error);font-size:9px}
.ok-icon{position:absolute;right:5px;top:18px;width:11px;height:11px;border-radius:50%;background:var(--ok);color:#fff;font-size:7px;line-height:11px;text-align:center}
.hint{font-size:6.5px;color:var(--label)}
.radio{display:inline-block;width:9px;height:9px;border:1px solid #bbb;border-radius:50%;vertical-align:middle;margin-right:4px;position:relative}
.radio.on::after{content:"";position:absolute;left:2px;top:2px;width:3px;height:3px;border-radius:50%;background:#555}
.step{display:inline-block;width:10px;height:10px;border:1px solid #ccc;border-radius:50%;font-size:7px;line-height:8px;text-align:center;color:#aaa;margin-right:6px}
.check{font-size:7.5px;color:var(--label);display:flex;align-items:center;gap:5px}
.box{width:9px;height:9px;border:1px solid #c8ced3;background:#fff}
.submit{left:113px;top:771px;width:545px;height:29px;background:var(--accent);color:#fff;font-size:8px;font-weight:700;display:flex;align-items:center;justify-content:center;border-radius:2px}
.cal{display:inline-block;width:10px;height:9px;border:1px solid #bbb;vertical-align:middle;margin-right:3px}
/* sidebar */
.sidebar{left:691px;top:257px;width:201px;height:380px;background:#f7fafb;border:1px solid #e4e9ec}
.side-price{left:776px;top:281px;font-size:20px;font-weight:700;color:var(--heading)}
.side-delivery{left:776px;top:303px;font-size:11px;color:var(--heading)}
.side-divider{left:691px;top:339px;width:201px;height:1px;background:#e4e9ec}
.side-item{left:749px;font-size:7px;color:#555d63;line-height:11px;width:110px}
.side-icon{left:712px;width:24px;height:20px;border:1px solid #b9c1c7;border-radius:3px}
.cert{left:712px;border-radius:6px}
/* footer */
.site-footer{left:0;top:854px;width:956px;height:102px;background:var(--footer)}
.foot-copy{left:112px;top:890px;font-size:6.5px;color:var(--footer-text)}
.foot-nav{left:439px;top:890px;font-size:6.5px;color:var(--footer-text);display:flex;gap:17px}
</style>
</head>
<body>
<main class="screen">
  <header class="abs site-header"></header>
  <div class="abs brand-dot"></div>
  <div class="abs brand-name">BrambleQuarry</div>
  <div class="abs brand-tld">.com</div>
  <div class="abs region-map" role="img" aria-label="Map of the state region"></div>
  <div class="abs promo">
    <span class="promo-line">Instant</span>
    <span class="promo-line">Delivery</span>
    <span class="promo-price">$7.95</span>
  </div>

  <h1 class="abs page-title">Salaried Employee</h1>
  <p class="abs page-sub">You will withhold taxes from this person and send them to the government.</p>

  <h2 class="abs section-title" style="left:110px;top:207px">Employer Information</h2>
  <div class="abs error-line"><span class="err-icon">×</span>COMPANY ZIP CODE</div>

  <div class="field" style="left:110px;top:260px;width:175px"><span class="label">Company Name*</span><span class="value">Marrow Pvt</span><span class="req">*</span></div>
  <div class="field" style="left:296px;top:260px;width:176px">Company Phone Number</div>
  <div class="field invalid" style="left:483px;top:260px;width:176px"><span class="label">Company Zip Code</span><span class="value">498754</span></div>
  <div class="field" style="left:110px;top:311px;width:175px">Company EIN / SSN</div>
  <div class="field" style="left:296px;top:311px;width:362px">Company Address</div>

  <h2 class="abs section-title" style="left:110px;top:387px">Employee Information</h2>
  <div class="field" style="left:110px;top:410px;width:175px">Employee Name*<span class="req">*</span></div>
  <div class="field" style="left:296px;top:410px;width:176px">Employee Address</div>
  <div class="field valid" style="left:483px;top:410px;width:176px"><span class="label" style="font-size:7.5px">Employee SSN</span><span class="value">4987</span><span class="req">*</span><span class="ok-icon">✓</span></div>
  <div class="abs hint" style="left:559px;top:448px;width:100px;text-align:right">Last 4 digits</div>
  <div class="field" style="left:110px;top:461px;width:175px">Employee ID</div>
  <div class="field" style="left:296px;top:461px;width:176px">Employee Zip Code</div>
  <div class="field" style="left:483px;top:461px;width:176px"><span class="label">Marital Status</span><span class="value"><span class="radio on"></span>Single<span class="radio" style="margin-left:24px"></span><span style="color:var(--label)">Married</span></span></div>
  <div class="field" style="left:110px;top:511px;width:175px"><span class="label">Number Of Dependants</span><span class="value"><span class="step">+</span>2</span></div>
  <div class="field" style="left:296px;top:511px;width:176px"><span class="label">Age 65 And Over / Blind Exemptions</span><span class="value"><span class="step">+</span>4</span></div>

  <h2 class="abs section-title" style="left:111px;top:580px">Salary Information</h2>
  <div class="field" style="left:110px;top:603px;width:175px">Annual Salary</div>
  <div class="field" style="left:296px;top:603px;width:176px"><span class="label">Pay Frequency</span><span class="value">Daily</span><span class="req">*</span><span style="position:absolute;right:9px;top:19px;font-size:7px">⌄</span></div>
  <div class="field" style="left:483px;top:603px;width:176px"></div>
  <div class="abs hint" style="left:370px;top:641px;width:100px;text-align:right">Pay Period</div>
  <div class="field" style="left:112px;top:654px;width:547px"><span class="label">Choose First Pay Date(s) Needed</span><span class="value"><span class="cal"></span>15 MAY 2016 <span class="cal" style="margin-left:6px"></span> 25 MAY 2016 <span style="color:var(--error)">⊗</span></span><span style="position:absolute;right:22px;top:6px;color:var(--link);font-size:7.5px">Add Next Paydate</span><span class="req">*</span></div>
  <div class="abs check" style="left:112px;top:701px"><span class="box"></span>This employee was hired in 2016</div>
  <div class="abs check" style="left:373px;top:701px"><span class="box"></span>Show hourly rate on the stub</div>

  <div class="abs submit">SUBMIT AL THE INFORMATION</div>

  <aside class="abs sidebar"></aside>
  <svg class="abs" style="left:711px;top:283px" width="62" height="32" viewBox="0 0 62 32">
    <g stroke="var(--envelope)" stroke-width="2" fill="none"><rect x="14" y="2" width="45" height="28"/><polyline points="14,2 36.5,19 59,2"/><polyline points="14,30 30,15"/><polyline points="59,30 43,15"/></g>
    <g stroke="var(--envelope)" stroke-width="2"><line x1="2" y1="12" x2="10" y2="12"/><line x1="5" y1="17" x2="10" y2="17"/><line x1="2" y1="22" x2="10" y2="22"/></g>
  </svg>
  <div class="abs side-price">$7.95</div>
  <div class="abs side-delivery">INSTANT DELIVERY</div>
  <div class="abs side-divider"></div>
  <div class="abs side-icon" style="top:357px"></div>
  <div class="abs side-item" style="top:358px">LOOKING FOR ANOTHER STATE?</div>
  <div class="abs side-icon" style="top:402px;border-radius:50%"></div>
  <div class="abs side-item" style="top:403px">PROBLEM WITH YOUR STUB DELIVERY?</div>
  <div class="abs side-icon" style="top:443px"></div>
  <div class="abs side-item" style="top:442px">TO SEE A FINISHED PAYSTUB SAMPLE.</div>
  <div class="abs cert" style="top:505px;width:103px;height:38px;background:#b8323a"></div>
  <div class="abs cert" style="top:574px;width:88px;height:35px;background:#2f6e3a;border:2px solid #222"></div>

  <footer class="abs site-footer"></footer>
  <div class="abs foot-copy">© COPYRIGHT BRAMBLEQUARRY.COM. ALL RIGHTS RESERVED.</div>
  <nav class="abs foot-nav"><span>ABOUT US</span><span>FEATURES</span><span>FAQ</span><span>CONTACT</span><span>LEGAL DOCUMENTS</span><span>ACCEPTABLE USE POLICY</span></nav>
</main>
</body>
</html>
```